Dunvarra windows & Home Improvements

We are a family run business with over 35 years expertise. Myself and father run it
We supply and install a rated windows and all types of doors and
Verandel composite doors .
We also specialise in renovating houses and adding extensions on to houses .
Are biggest selling point is the quality of the products we provide . we give 15 year guarantee on all windows and doors

I need flyers to distribute at shows and also to put through letterboxes
they can be a6 or a5 which ever works best . I have attached some images and our logo. Images don't have to be used

I have a show on the 29th march so need them fairly fast. Been designing them myself on this but they just don't look right

```html
<!DOCTYPE html>
<html lang="en">
<head>
<meta charset="utf-8">
<title>Dunvarra Windows &amp; Home Improvements – Flyer</title>
<link href="https://fonts.googleapis.com/css2?family=Oswald:wght@400;600;700&family=Dancing+Script:wght@700&display=swap" rel="stylesheet">
<style>
  :root {
    --stage: #3a3a3c;
    --teal-deep: #0a6f78;
    --teal: #14a3ad;
    --teal-light: #3cc7cf;
    --white: #ffffff;
    --paper-edge: #e9eef0;
    --photo-wall: #d9dbdc;
    --photo-floor: #b49a82;
    --ring: #f2f4f5;
  }
  * { margin: 0; padding: 0; box-sizing: border-box; }
  html, body {
    width: 1200px; height: 927px; overflow: hidden;
    background: var(--stage);
  }
  .flyer {
    position: absolute;
    left: 150px; top: 110px;
    width: 900px; height: 707px;
    background: var(--paper-edge);
    display: grid;
    grid-template-columns: 330px 1fr;
    font-family: "Oswald", sans-serif;
    color: var(--white);
    box-shadow: 0 20px 50px rgba(0,0,0,.45);
  }
  .flyer__photo {
    background: linear-gradient(180deg, var(--photo-wall) 0%, var(--photo-wall) 72%, var(--photo-floor) 72%, #9c8169 100%);
  }
  .flyer__body {
    position: relative;
    margin: 22px 22px 22px 0;
    background: radial-gradient(ellipse at 40% 45%, var(--teal-light) 0%, var(--teal) 45%, var(--teal-deep) 100%);
    padding: 40px 44px;
  }
  .brand {
    display: flex; align-items: center; gap: 12px;
    font-weight: 600; font-size: 24px; letter-spacing: 1px; text-transform: uppercase;
  }
  .brand__mark { width: 22px; height: 22px; background: var(--white); }
  .services {
    position: absolute; right: 44px; top: 110px;
    display: flex; flex-direction: column; gap: 22px;
  }
  .services__item {
    width: 118px; height: 118px; border-radius: 50%;
    border: 9px solid var(--ring);
    background: var(--teal);
    box-shadow: 0 4px 12px rgba(0,0,0,.25);
  }
  .tagline {
    margin-top: 44px; max-width: 330px;
    font-size: 19px; line-height: 1.35; letter-spacing: 1px; text-transform: uppercase;
  }
  .experience {
    position: absolute; left: 44px; bottom: 54px;
    text-transform: uppercase; line-height: .95;
  }
  .experience__stars { display: block; width: 150px; height: 20px; margin-bottom: 6px; }
  .experience__over {
    font-family: "Dancing Script", cursive; text-transform: none;
    font-size: 44px;
  }
  .experience__years { display: block; font-size: 86px; font-weight: 700; }
  .experience__expertise { display: block; font-size: 50px; font-weight: 600; letter-spacing: 2px; }
</style>
</head>
<body>
  <article class="flyer">
    <div class="flyer__photo" role="img" aria-label="Photo of a white panelled front door above a wooden floor, with a 15 year guarantee sticker"></div>
    <section class="flyer__body">
      <header class="brand">
        <span class="brand__mark"></span>
        <span class="brand__name">Dunvarra Windows &amp; Home Improvements</span>
      </header>
      <p class="tagline">Supply and install A rated windows, all types of doors and Verandel composite doors</p>
      <div class="services">
        <div class="services__item" role="img" aria-label="Window illustration"></div>
        <div class="services__item" role="img" aria-label="Front door illustration"></div>
        <div class="services__item" role="img" aria-label="Arched window illustration"></div>
      </div>
      <div class="experience">
        <svg class="experience__stars" viewBox="0 0 150 20" aria-hidden="true">
          <g fill="#ffffff">
            <polygon points="10,2 12.4,8 19,8 13.6,12 15.6,18.5 10,14.5 4.4,18.5 6.4,12 1,8 7.6,8"/>
            <polygon points="40,2 42.4,8 49,8 43.6,12 45.6,18.5 40,14.5 34.4,18.5 36.4,12 31,8 37.6,8"/>
            <polygon points="70,2 72.4,8 79,8 73.6,12 75.6,18.5 70,14.5 64.4,18.5 66.4,12 61,8 67.6,8"/>
          </g>
        </svg>
        <span class="experience__over">Over</span>
        <span class="experience__years">35 Years</span>
        <span class="experience__expertise">of Expertise</span>
      </div>
    </section>
  </article>
</body>
</html>
```